Wordpress Template for Food Retail Shop

We need a wordpress template that fits our new wp installation with about 6-7 sites. frontpage, news, team, products, contact. we provide food from local suppliers, * green * products. we provide a local bakery

```html
<!DOCTYPE html>
<html lang="en">
<head>
<meta charset="utf-8">
<title>Fennora Market – Local Green Food</title>
<link rel="stylesheet" href="https://fonts.googleapis.com/css2?family=Montserrat:wght@400;600;700&family=Open+Sans:wght@400;600&display=swap">
<style>
:root{
  --green:#7cbf2e;
  --green-dark:#5e9e1c;
  --orange:#f5a11f;
  --orange-dark:#e88a0c;
  --ink:#2b2b2b;
  --muted:#7a7a7a;
  --cream:#f8f9ea;
  --white:#ffffff;
  --black:#111111;
}
*{box-sizing:border-box;margin:0;padding:0}
html,body{width:1200px;height:4216px;overflow:hidden}
body{font-family:"Open Sans",Arial,sans-serif;color:var(--ink);background:var(--white);position:relative}
.abs{position:absolute}
h1,h2,h3,h4{font-family:"Montserrat",Arial,sans-serif}

/* header */
.site-header{left:0;top:0;width:1200px;height:120px;background:var(--white)}
.brand{left:90px;top:30px;display:flex;align-items:center;gap:14px}
.brand-mark{width:52px;height:52px;border-radius:50%;background:var(--green)}
.brand-name{font-family:"Montserrat",sans-serif;font-weight:700;font-size:40px;color:var(--green);letter-spacing:1px}
.main-nav{right:80px;top:44px;display:flex;gap:52px;font-family:"Montserrat",sans-serif;font-size:19px;font-weight:600;color:#444}
.main-nav .active{color:var(--orange)}

/* hero */
.hero{left:0;top:120px;width:1200px;height:760px;overflow:hidden}
.hero-photo{position:absolute;inset:0;background:linear-gradient(110deg,#3d5a2a 0%,#5c7b35 40%,#8a6a35 65%,#4a6b2c 100%)}
.hero-brand{left:100px;top:150px;display:flex;align-items:center;gap:20px}
.hero-brand .brand-mark{width:110px;height:110px;background:var(--white)}
.hero-brand .brand-name{font-size:84px;color:var(--white)}
.hero-text{left:100px;top:286px;width:520px;font-size:18px;line-height:1.45;color:var(--white);font-weight:600}
.btn{display:inline-block;background:var(--orange);color:var(--white);font-family:"Montserrat",sans-serif;font-weight:600;font-size:17px;border-radius:24px;padding:12px 28px;text-transform:uppercase}
.hero .btn{position:absolute;left:100px;top:382px}
.dots{display:flex;gap:14px}
.dots span{width:12px;height:12px;border-radius:50%;background:rgba(255,255,255,.6)}
.dots span.on{background:var(--white)}
.hero .dots{position:absolute;left:528px;top:514px}
.hero-wave{left:0;top:700px;width:1200px;height:180px}

/* welcome */
.section-title{width:1200px;text-align:center;font-size:48px;font-weight:600;letter-spacing:2px;color:var(--ink)}
.section-title em{font-style:normal;color:var(--green)}
.welcome-title{left:0;top:940px}
.feature{width:250px;text-align:center}
.feature-icon{width:84px;height:84px;border-radius:50%;border:3px solid #f7c78a;margin:0 auto 14px;display:flex;align-items:center;justify-content:center}
.feature h3{font-size:21px;font-weight:700;margin-bottom:8px}
.feature p{font-size:13px;color:var(--muted);line-height:1.5}
.welcome-photo{left:380px;top:1060px;width:440px;height:380px;border-radius:50%;background:radial-gradient(circle,#c74a2a 0%,#e07a32 30%,#6fa33a 60%,#f4f4f4 72%)}

/* products */
.products{left:0;top:1580px;width:1200px;height:780px;overflow:hidden}
.products-bg{position:absolute;inset:0;background:linear-gradient(180deg,var(--green) 0%,var(--green-dark) 100%)}
.products-wave{left:0;top:1560px;width:1200px;height:120px}
.products-title{left:0;top:1735px;color:var(--white);font-weight:400}
.products-title strong{font-weight:700}
.products-intro{left:330px;top:1808px;width:540px;text-align:center;font-size:13px;color:#eaf6d8;line-height:1.5}
.product{width:240px;text-align:center;color:var(--white)}
.product-photo{width:220px;height:220px;border-radius:50%;border:7px solid var(--orange);margin:0 auto 18px}
.product h4{font-size:20px;font-weight:700;margin-bottom:8px}
.product p{font-size:13px;line-height:1.5;color:#eef7e0;padding:0 30px}

/* split blocks */
.panel-photo{width:600px;height:510px}
.panel-text{width:600px;height:510px;background:var(--cream);text-align:center;padding:0 90px;display:flex;flex-direction:column;justify-content:center;align-items:center}
.panel-text h3{font-size:27px;font-weight:600;margin-bottom:26px}
.panel-text p{font-size:16px;line-height:1.6;color:#555;margin-bottom:28px}

/* testimonials */
.quote{width:300px;text-align:center}
.avatar{width:92px;height:92px;border-radius:50%;background:linear-gradient(160deg,#c9b8a4,#8c7462);margin:0 auto 40px}
.quote p{font-size:14px;color:var(--muted);line-height:1.5;margin-bottom:18px}
.quote h4{font-size:16px;font-weight:700}
.testi-dots{left:576px;top:3748px}
.testi-dots span{background:#cfe6b5}
.testi-dots span.on{background:var(--green)}

/* contact bar */
.contact-bar{left:0;top:3860px;width:1200px;height:200px;background:var(--orange);color:var(--white)}
.contact-item{top:70px;display:flex;align-items:center;gap:20px;font-size:15px;line-height:1.5}
.contact-icon{width:58px;height:58px;border-radius:50%;border:2px solid var(--white);display:flex;align-items:center;justify-content:center;flex:none}

/* footer */
.site-footer{left:0;top:4060px;width:1200px;height:156px;background:var(--black);color:#ccc;text-align:center}
.social{position:absolute;left:476px;top:22px;display:flex;gap:24px}
.social span{width:24px;height:24px;border-radius:4px;background:#e8e8e8}
.footer-nav{position:absolute;left:0;top:82px;width:1200px;display:flex;justify-content:center;gap:30px;font-size:15px;color:#eee}
.footer-nav i{font-style:normal;color:#777}
.copyright{position:absolute;left:0;top:122px;width:1200px;font-size:13px;color:#999}
</style>
</head>
<body>

<header class="site-header abs">
  <div class="brand abs"><span class="brand-mark"></span><span class="brand-name">FENNORA</span></div>
  <nav class="main-nav abs"><span class="active">HOME</span><span>NEWS</span><span>TEAM</span><span>PRODUCTS</span><span>CONTACT</span></nav>
</header>

<section class="hero abs">
  <div class="hero-photo" role="img" aria-label="Garden scene with a wicker basket of fresh beans, tomatoes and greens"></div>
  <div class="hero-brand abs"><span class="brand-mark"></span><span class="brand-name">FENNORA</span></div>
  <p class="hero-text abs">Lorem ipsum dolor sit amet, consectetur adipiscing elit, sed do eiusmod tempor incididunt ut</p>
  <span class="btn">Learn more</span>
  <div class="dots"><span class="on"></span><span></span><span></span><span></span></div>
</section>
<svg class="hero-wave abs" viewBox="0 0 1200 180" preserveAspectRatio="none" aria-hidden="true">
  <path d="M0 120 C300 40 700 200 1200 60 L1200 180 L0 180Z" fill="#fff"/>
  <path d="M0 130 C300 60 700 210 1200 70" fill="none" stroke="#f5a11f" stroke-width="10"/>
</svg>

<h2 class="section-title welcome-title abs">WELCOME TO <em>FENNORA</em></h2>
<div class="welcome-photo abs" role="img" aria-label="Basket overflowing with fresh vegetables and fruit"></div>

<div class="feature abs" style="left:110px;top:1030px">
  <div class="feature-icon"><svg width="40" height="40" viewBox="0 0 40 40"><path d="M8 30 C8 14 20 8 32 8 C32 22 24 32 8 30Z" fill="none" stroke="#f5a11f" stroke-width="3"/></svg></div>
  <h3>100% ORGANIC</h3>
  <p>Sed ut perspiciatis unde omnis iste natus error sit ...</p>
</div>
<div class="feature abs" style="left:110px;top:1250px">
  <div class="feature-icon"><svg width="40" height="40" viewBox="0 0 40 40"><circle cx="14" cy="14" r="6" fill="none" stroke="#f5a11f" stroke-width="3"/><circle cx="27" cy="16" r="5" fill="none" stroke="#f5a11f" stroke-width="3"/><path d="M4 34 C4 24 24 24 24 34M20 34 C20 26 36 26 36 34" fill="none" stroke="#f5a11f" stroke-width="3"/></svg></div>
  <h3>HEALTHY FAMILY</h3>
  <p>Sed ut perspiciatis unde omnis iste natus error sit ...</p>
</div>
<div class="feature abs" style="left:840px;top:1030px">
  <div class="feature-icon"><svg width="40" height="40" viewBox="0 0 40 40"><circle cx="20" cy="20" r="14" fill="none" stroke="#f5a11f" stroke-width="3"/><path d="M20 11 V20 L27 24" fill="none" stroke="#f5a11f" stroke-width="3"/></svg></div>
  <h3>ALWAYS FRESH</h3>
  <p>Sed ut perspiciatis unde omnis iste natus error sit ...</p>
</div>
<div class="feature abs" style="left:840px;top:1250px">
  <div class="feature-icon"><svg width="40" height="40" viewBox="0 0 40 40"><path d="M20 5 L33 10 V20 C33 28 27 33 20 36 C13 33 7 28 7 20 V10Z" fill="none" stroke="#f5a11f" stroke-width="3"/><path d="M14 20 L19 25 L27 15" fill="none" stroke="#f5a11f" stroke-width="3"/></svg></div>
  <h3>FOOD SAFETY</h3>
  <p>Sed ut perspiciatis unde omnis iste natus error sit ...</p>
</div>

<section class="products abs">
  <div class="products-bg"></div>
</section>
<svg class="products-wave abs" viewBox="0 0 1200 120" preserveAspectRatio="none" aria-hidden="true">
  <path d="M0 0 H1200 V50 C800 110 400 0 0 70Z" fill="#fff"/>
  <path d="M0 60 C400 -10 800 100 1200 40" fill="none" stroke="#f5a11f" stroke-width="12"/>
</svg>
<h2 class="section-title products-title abs">OUR <strong>PRODUCTS</strong></h2>
<p class="products-intro abs">Sed ut perspiciatis unde omnis iste natus error sit voluptatem accusantium doloremque laudantium totam rem aperiam.</p>

<div class="product abs" style="left:70px;top:1910px">
  <div class="product-photo" role="img" aria-label="Freshly baked bread slices" style="background:linear-gradient(135deg,#c98a4a,#7a4a22)"></div>
  <h4>LOREM IPSUM</h4><p>Ut enim ad minima veniam, quis nostrum</p>
</div>
<div class="product abs" style="left:343px;top:1910px">
  <div class="product-photo" role="img" aria-label="Fresh tomatoes and vegetables" style="background:linear-gradient(135deg,#d8452e,#6fa33a)"></div>
  <h4>LOREM IPSUM</h4><p>Ut enim ad minima veniam, quis nostrum</p>
</div>
<div class="product abs" style="left:616px;top:1910px">
  <div class="product-photo" role="img" aria-label="Bowls of grains and dairy" style="background:linear-gradient(135deg,#efe4cf,#b59a74)"></div>
  <h4>LOREM IPSUM</h4><p>Ut enim ad minima veniam, quis nostrum</p>
</div>
<div class="product abs" style="left:889px;top:1910px">
  <div class="product-photo" role="img" aria-label="Plate of fresh green salad" style="background:linear-gradient(135deg,#9cc861,#4b7e2a)"></div>
  <h4>LOREM IPSUM</h4><p>Ut enim ad minima veniam, quis nostrum</p>
</div>

<div class="panel-photo abs" style="left:0;top:2355px;background:linear-gradient(135deg,#6b4a2c,#b0412a 40%,#5e8a2e 75%,#3f3a2a)" role="img" aria-label="Hands holding a crate of colourful fresh vegetables"></div>
<div class="panel-text abs" style="left:600px;top:2355px">
  <h3>About Us</h3>
  <p>Lorem ipsum dolor sit amet, consectetur adipiscing elit, sed do eiusmod tempor incididunt ut labore et dolore magna aliqua. Ut enim ad minim veniam, quis nostrud exercitation ullamco laboris nisi ut aliquip ex ea commodo consequat.</p>
  <span class="btn">Read more</span>
</div>
<div class="panel-text abs" style="left:0;top:2865px">
  <h3>Team</h3>
  <p>Lorem ipsum dolor sit amet, consectetur adipiscing elit, sed do eiusmod tempor incididunt ut labore et dolore magna aliqua. Ut enim ad minim veniam, quis nostrud exercitation ullamco laboris nisi ut aliquip ex ea commodo consequat.</p>
  <span class="btn">Meet our team</span>
</div>
<div class="panel-photo abs" style="left:600px;top:2865px;background:linear-gradient(135deg,#2f4a1e,#5d8a2c 45%,#d76a2a 70%,#3a5a22)" role="img" aria-label="Crate of leafy greens, carrots and asparagus"></div>

<div class="quote abs" style="left:50px;top:3490px">
  <div class="avatar" role="img" aria-label="Customer portrait"></div>
  <p>Sed ut perspiciatis unde omnis iste natus error sit voluptatem</p><h4>-MARO</h4>
</div>
<div class="quote abs" style="left:450px;top:3490px">
  <div class="avatar" role="img" aria-label="Customer portrait"></div>
  <p>Sed ut perspiciatis unde omnis iste natus error sit voluptatem</p><h4>-LINA</h4>
</div>
<div class="quote abs" style="left:850px;top:3490px">
  <div class="avatar" role="img" aria-label="Customer portrait"></div>
  <p>Sed ut perspiciatis unde omnis iste natus error sit voluptatem</p><h4>-TEODOR</h4>
</div>
<div class="dots testi-dots abs"><span class="on"></span><span></span><span></span></div>

<section class="contact-bar abs">
  <div class="contact-item abs" style="left:90px">
    <span class="contact-icon"><svg width="24" height="28" viewBox="0 0 24 28"><path d="M12 26 C4 16 3 13 3 10 A9 9 0 0 1 21 10 C21 13 20 16 12 26Z" fill="none" stroke="#fff" stroke-width="2.5"/><circle cx="12" cy="10" r="3" fill="#fff"/></svg></span>
    <span>Fennora<br>Greenway 14, 10115 Oakfield</span>
  </div>
  <div class="contact-item abs" style="left:490px">
    <span class="contact-icon"><svg width="26" height="26" viewBox="0 0 26 26"><path d="M6 3 L10 3 L12 9 L9 11 C10 14 12 16 15 17 L17 14 L23 16 L23 20 C23 22 21 23 19 23 C10 22 4 16 3 7 C3 5 4 3 6 3Z" fill="none" stroke="#fff" stroke-width="2.2"/></svg></span>
    <span>Phone<br>+1 (555) 010 4477</span>
  </div>
  <div class="contact-item abs" style="left:890px">
    <span class="contact-icon"><svg width="28" height="22" viewBox="0 0 28 22"><rect x="2" y="2" width="24" height="18" rx="2" fill="none" stroke="#fff" stroke-width="2.2"/><path d="M2 4 L14 13 L26 4" fill="none" stroke="#fff" stroke-width="2.2"/></svg></span>
    <span>E-mail<br>hello@fennoramarket.test</span>
  </div>
</section>

<footer class="site-footer abs">
  <div class="social"><span></span><span></span><span></span><span></span><span></span></div>
  <nav class="footer-nav"><span>Home</span><i>|</i><span>News</span><i>|</i><span>Team</span><i>|</i><span>Products</span><i>|</i><span>Contact</span></nav>
  <p class="copyright">Copyright © 2019 Fennora Market. All Rights Reserved.</p>
</footer>

</body>
</html>
```